Higher co-efficient of performance means more heat for your money

I need a bar graph that will have the following heating systems, 80% efficient gas furnace COP of .8, Electric heat COP of 1, and Our best selling heat pump with a cop of 4 at 47F. I will have a constant bar, 100$ worth of gas for furnace, 100$ of electricity for electric heat, and 100$ worth of electricity for our heat pumps. next to them I will have a bar showing how much heat each heating system will provide for $100 of fuel. For gas furnace I need a bar that says $80 worth of heat and the barograph to match it, for electric heat I need the bar to show 100$ worth of heat, for our best selling heat pump I need the bar graph to show and say $400 dollars worth of heat. Please take a look at my website www.summitbreezecomfort.example for brand color and feel

```html
<!DOCTYPE html>
<html lang="en">
<head>
<meta charset="utf-8">
<title>Higher Coefficient of Performance — Summit Breeze Comfort</title>
<link rel="stylesheet" href="https://fonts.googleapis.com/css2?family=Montserrat:wght@700;800&display=swap">
<style>
  :root {
    --brand-blue: #0a6fbe;
    --brand-blue-light: #1c80cc;
    --brand-red: #e31b2b;
    --brand-red-light: #ec2f3d;
    --white: #ffffff;
    --title-font: "Montserrat", Arial, sans-serif;
  }
  html, body {
    margin: 0;
    padding: 0;
    width: 1200px;
    height: 1200px;
    overflow: hidden;
    background: var(--white);
  }
  .poster {
    position: relative;
    width: 1200px;
    height: 1200px;
    overflow: hidden;
    font-family: var(--title-font);
    background: var(--white);
  }
  .header-shapes {
    position: absolute;
    left: 0;
    top: 0;
  }
  .headline {
    position: absolute;
    left: 62px;
    top: 40px;
    margin: 0;
    color: var(--white);
    font-weight: 800;
    font-size: 36px;
    line-height: 49px;
    letter-spacing: 0.5px;
    text-transform: uppercase;
  }
  .footnote {
    position: absolute;
    left: 54px;
    top: 208px;
    margin: 0;
    color: var(--white);
    font-weight: 700;
    font-size: 23px;
    letter-spacing: 0.5px;
  }
  .brand {
    position: absolute;
    left: 830px;
    top: 150px;
    width: 330px;
    text-align: center;
    color: var(--brand-blue);
    font-weight: 800;
    font-size: 34px;
    line-height: 40px;
    text-transform: uppercase;
  }
  .brand-dot {
    display: block;
    width: 54px;
    height: 54px;
    margin: 0 auto 14px;
    border-radius: 50%;
    background: var(--brand-red);
  }
  .bar {
    position: absolute;
    bottom: 132px;
    width: 106px;
    color: var(--white);
    text-align: center;
    font-weight: 800;
    text-transform: uppercase;
  }
  .bar--input {
    background: linear-gradient(90deg, var(--brand-blue) 0 50%, var(--brand-blue-light) 50% 100%);
  }
  .bar--output {
    background: linear-gradient(90deg, var(--brand-red) 0 50%, var(--brand-red-light) 50% 100%);
  }
  .bar-label {
    position: absolute;
    left: 0;
    right: 0;
    line-height: 1;
  }
  .bar-value {
    display: block;
    font-size: 31px;
  }
  .bar-small {
    display: block;
    font-size: 13px;
    margin-top: 3px;
  }
  .bar-unit {
    display: block;
    font-size: 22px;
    margin-top: 1px;
  }
  .bar-word {
    display: block;
    font-size: 20px;
    margin-top: 2px;
  }
  .baseline {
    position: absolute;
    left: 0;
    bottom: 0;
    width: 1200px;
    height: 132px;
    background: var(--brand-blue);
  }
  .category {
    position: absolute;
    top: 26px;
    margin: 0;
    color: var(--white);
    font-weight: 800;
    font-size: 29px;
    line-height: 33px;
    text-align: center;
    text-transform: uppercase;
    transform: translateX(-50%);
    white-space: nowrap;
  }
</style>
</head>
<body>
<main class="poster">
  <svg class="header-shapes" width="1200" height="300" viewBox="0 0 1200 300" aria-hidden="true">
    <polygon points="0,0 786,0 666,290 0,290" fill="var(--brand-blue)"/>
    <polygon points="794,0 818,0 712,258 688,258" fill="var(--brand-red)"/>
  </svg>

  <h1 class="headline">Higher co-efficient of<br>performance means more<br>heat for your money</h1>
  <p class="footnote">*COP MEASURE OF 47°F</p>

  <div class="brand">
    <span class="brand-dot"></span>
    Summit Breeze<br>Comfort
  </div>

  <!-- Gas furnace -->
  <div class="bar bar--input" style="left:34px; height:274px;">
    <div class="bar-label" style="top:80px;">
      <span class="bar-value">100</span>
      <span class="bar-small">of</span>
      <span class="bar-unit">Gas</span>
    </div>
  </div>
  <div class="bar bar--output" style="left:180px; height:216px;">
    <div class="bar-label" style="top:80px;">
      <span class="bar-value">80</span>
      <span class="bar-small">of</span>
      <span class="bar-unit">Heat</span>
    </div>
  </div>

  <!-- Electric heat -->
  <div class="bar bar--input" style="left:460px; height:274px;">
    <div class="bar-label" style="top:74px;">
      <span class="bar-value">100</span>
      <span class="bar-small">of</span>
      <span class="bar-unit">Elect.</span>
    </div>
  </div>
  <div class="bar bar--output" style="left:612px; height:274px;">
    <div class="bar-label" style="top:74px;">
      <span class="bar-value">100</span>
      <span class="bar-small">of</span>
      <span class="bar-unit">Heat</span>
    </div>
  </div>

  <!-- Heat pump -->
  <div class="bar bar--input" style="left:852px; height:274px;">
    <div class="bar-label" style="top:74px;">
      <span class="bar-value">100</span>
      <span class="bar-small">of</span>
      <span class="bar-unit">Elect.</span>
    </div>
  </div>
  <div class="bar bar--output" style="left:996px; height:570px;">
    <div class="bar-label" style="top:86px;">
      <span class="bar-value">400</span>
      <span class="bar-word">Work</span>
      <span class="bar-word">of</span>
      <span class="bar-word">Heat</span>
    </div>
  </div>

  <footer class="baseline">
    <p class="category" style="left:150px;">80%<br>Gas furnace</p>
    <p class="category" style="left:590px;">Electric<br>heat</p>
    <p class="category" style="left:972px;">Our best<br>selling heat pump</p>
  </footer>
</main>
</body>
</html>
```